Candle Rental Business seeks new website design

We need a new website design for a Candle hire business. The business rents out pillar candles for events such as weddings and corporate events. Our main target market is weddings. The business name is Hire a Lantern. The business name does not have a logo design.

We would like a website that is light in colours and creates a warm atmosphere. The design needs to be elegant and upmarket. There are different size candles that we hire out, ranging from 10cm diameter to 20cm diameter, flat, tall etc. All our candles are white in colour. Its just the size that differs.

We would also like to include a section for hiring out decor such as glassvases, candlebras, overlays and chairs sachets, chair covers. However, this is not the businesses main focus but an additional offering to customers.

Target Market(s)

Wedding venues and brides. Corporate events. School dances.

Industry/Entity Type

Hospitality

Logo Text

Hire a Lantern

Number of Pages Required

1 page

Font styles to use
Sans Serif
Script

Requirements
Must have
• Pictures of pillar candles. Plain white candles. The website must centre around candles.
Nice to have
• Different examples of candle centrepieces
Should not have
• Pictures must not be of brides. Pictures of surrounding is perferable.

```html
<!DOCTYPE html>
<html lang="en">
<head>
<meta charset="utf-8">
<title>Hire a Lantern</title>
<link rel="stylesheet" href="https://fonts.googleapis.com/css2?family=Raleway:wght@500;600;700&family=Open+Sans:ital,wght@0,400;0,600;0,700;1,400&display=swap">
<style>
:root{
  --red:#e8311a;
  --red-dark:#c92812;
  --ink:#555;
  --ink-soft:#777;
  --heading:#5a5a5a;
  --line:#e6e6e6;
  --night:#0e0b0a;
  --white:#fff;
}
*{box-sizing:border-box;margin:0;padding:0}
html,body{width:1200px;height:2317px;overflow:hidden}
body{position:relative;background:var(--white);font-family:"Open Sans",Arial,sans-serif;color:var(--ink)}
.abs{position:absolute}
a{color:inherit;text-decoration:none}

/* header */
.site-header{position:absolute;left:0;top:0;width:1200px;height:78px;background:var(--white)}
.brand{position:absolute;left:99px;top:22px;display:flex;align-items:center;gap:12px}
.brand-mark{width:34px;height:34px;background:var(--red)}
.brand-name{font-family:"Open Sans",Arial,sans-serif;font-size:27px;font-weight:400;color:#333;letter-spacing:-.5px}
.main-nav{position:absolute;right:97px;top:0;display:flex;height:78px}
.main-nav a{display:flex;align-items:center;padding:0 24px;font-size:13px;color:#666;position:relative}
.main-nav a.active{color:#333}
.main-nav a.active::after{content:"";position:absolute;left:24px;right:24px;bottom:0;height:3px;background:var(--red)}

/* hero */
.hero{position:absolute;left:0;top:78px;width:1200px;height:466px;
  background:radial-gradient(ellipse at 68% 45%,#c8652a 0%,#7a2a12 30%,#2a0f08 62%,#140807 100%)}
.hero-title{position:absolute;left:99px;top:148px;font-family:"Open Sans",Arial,sans-serif;font-weight:600;font-size:31px;color:var(--white)}
.hero-text{position:absolute;left:99px;top:198px;width:430px;font-size:16px;line-height:28px;color:var(--white)}
.btn-red{display:inline-flex;align-items:center;justify-content:center;background:var(--red);color:var(--white);font-weight:600;text-transform:uppercase}
.hero .btn-red{position:absolute;left:99px;top:279px;width:182px;height:43px;font-size:13px;border-radius:2px}
.dots{display:flex;gap:6px}
.dots span{width:7px;height:7px;border-radius:50%;background:rgba(255,255,255,.45)}
.dots span.on{background:var(--red)}
.hero .dots{position:absolute;left:580px;top:440px}

/* features */
.features{position:absolute;left:0;top:544px;width:1200px;height:116px;border-bottom:1px solid var(--line)}
.feature{position:absolute;top:22px;width:300px;display:flex;gap:14px}
.feature-icon{flex:none;width:50px;height:50px;border-radius:50%;background:var(--red);display:flex;align-items:center;justify-content:center}
.feature h3{font-size:12px;font-weight:700;color:var(--red);margin-top:6px}
.feature p{font-size:11.5px;line-height:23px;color:var(--ink-soft);margin-top:2px}

/* welcome */
.welcome-frame{position:absolute;left:99px;top:706px;width:380px;height:260px;border:1px solid #ddd;padding:9px;background:var(--white);box-shadow:0 1px 3px rgba(0,0,0,.06)}
.welcome-photo{width:100%;height:100%;background:linear-gradient(135deg,#2c2a2a 0%,#4a3a30 45%,#cfc7bd 75%,#e9e6e1 100%)}
.welcome-text{position:absolute;left:528px;top:714px;width:575px}
.section-title{font-family:"Raleway",Arial,sans-serif;font-weight:600;font-size:23px;color:var(--heading);text-transform:uppercase}
.welcome-text p{margin-top:14px;font-size:11.5px;line-height:23px;color:var(--ink-soft)}
.ticks{list-style:none;margin-top:12px}
.ticks li{display:flex;align-items:center;gap:12px;font-size:11.5px;font-weight:600;color:#444;height:32px}

/* services */
.providing-head{position:absolute;left:0;top:1014px;width:1200px;text-align:center}
.providing-head p{font-size:12px;color:var(--ink-soft);margin-top:12px}
.tile{position:absolute;width:310px;height:232px}
.tile-photo{width:100%;height:100%}
.tile-label{position:absolute;left:0;bottom:0;width:190px;height:63px;background:var(--red);color:var(--white);padding:14px 0 0 18px}
.tile-label h4{font-size:13px;font-weight:700;text-transform:uppercase}
.tile-label span{display:flex;align-items:center;gap:5px;font-size:10px;margin-top:4px}

/* testimonials */
.testimonials{position:absolute;left:0;top:1668px;width:1200px;height:312px;
  background:radial-gradient(circle at 20% 30%,#4a3322 0%,transparent 18%),radial-gradient(circle at 80% 60%,#3e2b1d 0%,transparent 22%),radial-gradient(circle at 55% 90%,#5a2616 0%,transparent 25%),var(--night)}
.testimonials .section-title{position:absolute;left:0;top:46px;width:1200px;text-align:center;color:var(--white)}
.quote{position:absolute;top:127px;display:flex;gap:30px}
.avatar{flex:none;width:116px;height:116px;border-radius:50%;border:3px solid rgba(255,255,255,.85);background:linear-gradient(160deg,#c9a488,#7a5a46)}
.quote-body{position:relative;width:290px;padding-top:6px}
.quote-body p{font-size:11.5px;font-style:italic;line-height:22px;color:var(--white)}
.quote-body .name{display:block;margin-top:10px;font-size:10.5px;font-weight:700;color:var(--red);text-transform:uppercase}
.quote-body .role{display:block;font-size:10.5px;color:#999;margin-top:2px}
.qmark{position:absolute;font-family:Georgia,serif;font-size:34px;color:#888;line-height:1}
.testimonials .dots{position:absolute;left:585px;top:276px}
.testimonials .dots span{background:#555}
.testimonials .dots span.on{background:var(--red)}

/* footer */
.site-footer{position:absolute;left:0;top:1980px;width:1200px;height:263px;background:var(--red);color:var(--white)}
.fcol{position:absolute;top:38px}
.fcol h5{font-size:16px;font-weight:600}
.fcol p,.fcol li{font-size:11.5px;line-height:22px}
.fcol ul{list-style:none;margin-top:8px}
.email-field{margin-top:12px;width:307px;height:33px;background:var(--red-dark);font-size:11.5px;padding:0 15px;display:flex;align-items:center}
.btn-outline{margin-top:11px;width:112px;height:32px;border:1px solid var(--white);font-size:9.5px;font-weight:700;display:flex;align-items:center;justify-content:center;text-transform:uppercase}
.contact-line{display:flex;align-items:center;gap:10px}
.socials{display:flex;gap:12px;margin-top:12px}
.socials span{width:27px;height:27px;border-radius:50%;background:var(--white)}

/* bottom bar */
.bottom-bar{position:absolute;left:0;top:2243px;width:1200px;height:74px;display:flex;align-items:center;justify-content:center;gap:14px;font-size:11px;color:#666}
</style>
</head>
<body>

<header class="site-header">
  <div class="brand"><span class="brand-mark"></span><span class="brand-name">Hire a Lantern</span></div>
  <nav class="main-nav">
    <a class="active" href="#">Home</a><a href="#">About us</a><a href="#">Services</a><a href="#">What we do</a><a href="#">Events</a><a href="#">Gallery</a><a href="#">Contact us</a>
  </nav>
</header>

<section class="hero">
  <div class="abs" style="left:0;top:0;width:1200px;height:466px" role="img" aria-label="Lit white pillar candles in a festive centrepiece with berries and pine cones"></div>
  <h1 class="hero-title">HIRE A LANTERN</h1>
  <p class="hero-text">We rent out pillar candles for events such as weddings and corporate events.</p>
  <a class="btn-red" href="#">Subscribe here</a>
  <div class="dots"><span class="on"></span><span></span><span></span><span></span></div>
</section>

<section class="features">
  <div class="feature" style="left:99px">
    <div class="feature-icon"><svg width="24" height="22" viewBox="0 0 24 22"><path d="M12 1 23 12h-4v9h-4v-6H9v6H5v-9H1z" fill="#fff"/></svg></div>
    <div><h3>EVENTS</h3><p>Lorem Ipsum is simply dummy text of the printing and typesetting industry.</p></div>
  </div>
  <div class="feature" style="left:452px">
    <div class="feature-icon"><svg width="26" height="18" viewBox="0 0 26 18"><circle cx="9" cy="10" r="6.5" fill="none" stroke="#fff" stroke-width="2.4"/><circle cx="17" cy="10" r="6.5" fill="none" stroke="#fff" stroke-width="2.4"/></svg></div>
    <div><h3>WEDDINGS</h3><p>Lorem Ipsum is simply dummy text of the printing and typesetting industry.</p></div>
  </div>
  <div class="feature" style="left:805px">
    <div class="feature-icon"><svg width="26" height="20" viewBox="0 0 26 20"><path d="M2 8l6-5 5 3 5-3 6 5-9 9z" fill="none" stroke="#fff" stroke-width="2.2" stroke-linejoin="round"/></svg></div>
    <div><h3>CORPORATE EVENTS</h3><p>Lorem Ipsum is simply dummy text of the printing and typesetting industry.</p></div>
  </div>
</section>

<div class="welcome-frame"><div class="welcome-photo" role="img" aria-label="Hands holding a lit white pillar candle"></div></div>
<section class="welcome-text">
  <h2 class="section-title">Welcome to Hire a Lantern</h2>
  <p>Lorem Ipsum is simply dummy text of the printing and typesetting industry. Lorem Ipsum has been the industry's standard dummy text ever since the 1500s, when an unknown printer took a galley of type and scrambled it to make a type specimen book. It has survived not only five centuries, but also the leap into electronic typesetting, remaining essentially unchanged.</p>
  <ul class="ticks">
    <li><svg width="10" height="9" viewBox="0 0 10 9"><path d="M1 5l3 3 5-7" fill="none" stroke="#e8311a" stroke-width="2"/></svg>Lorem Ipsum is simply dummy text of the printing and typesetting industry.</li>
    <li><svg width="10" height="9" viewBox="0 0 10 9"><path d="M1 5l3 3 5-7" fill="none" stroke="#e8311a" stroke-width="2"/></svg>Lorem Ipsum is simply dummy text of the printing and typesetting industry text of the printing.</li>
    <li><svg width="10" height="9" viewBox="0 0 10 9"><path d="M1 5l3 3 5-7" fill="none" stroke="#e8311a" stroke-width="2"/></svg>Lorem Ipsum is simply dummy text of the printing and typesetting industry.</li>
  </ul>
</section>

<section class="providing-head">
  <h2 class="section-title">Also we are providing</h2>
  <p>Lorem Ipsum is simply dummy text of the printing and typesetting industry. Lorem Ipsum has been the industry's standard</p>
</section>

<div class="tile" style="left:99px;top:1112px">
  <div class="tile-photo" role="img" aria-label="Glass vases with blue flowers" style="background:linear-gradient(180deg,#6b6e7a,#b9bcbf 60%,#8a8d8c)"></div>
  <div class="tile-label"><h4>Glassvases</h4><span>Click here for view details <svg width="9" height="9" viewBox="0 0 9 9"><circle cx="4.5" cy="4.5" r="4.5" fill="#fff"/><path d="M3.5 2.5l2 2-2 2" fill="none" stroke="#e8311a" stroke-width="1.3"/></svg></span></div>
</div>
<div class="tile" style="left:446px;top:1112px">
  <div class="tile-photo" role="img" aria-label="Candlebra with lit white candles" style="background:radial-gradient(circle at 60% 40%,#d89a4e,#5a2e14 50%,#1d0f08)"></div>
  <div class="tile-label"><h4>Candlebras</h4><span>Click here for view details <svg width="9" height="9" viewBox="0 0 9 9"><circle cx="4.5" cy="4.5" r="4.5" fill="#fff"/><path d="M3.5 2.5l2 2-2 2" fill="none" stroke="#e8311a" stroke-width="1.3"/></svg></span></div>
</div>
<div class="tile" style="left:792px;top:1112px">
  <div class="tile-photo" role="img" aria-label="Table with overlay, flowers and lantern" style="background:linear-gradient(160deg,#7c8a5e,#d7c6c2 55%,#a9a39a)"></div>
  <div class="tile-label"><h4>Overlays</h4><span>Click here for view details <svg width="9" height="9" viewBox="0 0 9 9"><circle cx="4.5" cy="4.5" r="4.5" fill="#fff"/><path d="M3.5 2.5l2 2-2 2" fill="none" stroke="#e8311a" stroke-width="1.3"/></svg></span></div>
</div>
<div class="tile" style="left:99px;top:1378px">
  <div class="tile-photo" role="img" aria-label="Red decorative cushions and hanging lamps" style="background:linear-gradient(150deg,#3a4a5a,#8c2a26 50%,#b03a30)"></div>
  <div class="tile-label"><h4>Chairs sachets</h4><span>Click here for view details <svg width="9" height="9" viewBox="0 0 9 9"><circle cx="4.5" cy="4.5" r="4.5" fill="#fff"/><path d="M3.5 2.5l2 2-2 2" fill="none" stroke="#e8311a" stroke-width="1.3"/></svg></span></div>
</div>
<div class="tile" style="left:446px;top:1378px">
  <div class="tile-photo" role="img" aria-label="Rows of chairs with white covers and ribbons" style="background:linear-gradient(180deg,#6e5c5e,#b8b3b4 55%,#8e8788)"></div>
  <div class="tile-label"><h4>Chair covers</h4><span>Click here for view details <svg width="9" height="9" viewBox="0 0 9 9"><circle cx="4.5" cy="4.5" r="4.5" fill="#fff"/><path d="M3.5 2.5l2 2-2 2" fill="none" stroke="#e8311a" stroke-width="1.3"/></svg></span></div>
</div>
<div class="tile" style="left:792px;top:1378px">
  <div class="tile-photo" role="img" aria-label="Flower centrepiece with white candles" style="background:linear-gradient(180deg,#e9ddd6,#e6b8c6 55%,#9fb070)"></div>
  <div class="tile-label"><h4>Glassvases</h4><span>Click here for view details <svg width="9" height="9" viewBox="0 0 9 9"><circle cx="4.5" cy="4.5" r="4.5" fill="#fff"/><path d="M3.5 2.5l2 2-2 2" fill="none" stroke="#e8311a" stroke-width="1.3"/></svg></span></div>
</div>

<section class="testimonials" role="img" aria-label="Warm blurred candle light background">
  <h2 class="section-title">What our client's say</h2>
  <div class="quote" style="left:128px">
    <div class="avatar" role="img" aria-label="Client portrait"></div>
    <div class="quote-body">
      <span class="qmark" style="left:-18px;top:-6px">“</span>
      <p>Lorem Ipsum is simply dummy text of the printing and typesetting industry. Lorem Ipsum has been the industry's standard dummy text ever...</p>
      <span class="qmark" style="right:0;top:56px">”</span>
      <span class="name">Marcus Hale</span><span class="role">Business man</span>
    </div>
  </div>
  <div class="quote" style="left:633px">
    <div class="avatar" role="img" aria-label="Client portrait"></div>
    <div class="quote-body">
      <span class="qmark" style="left:-18px;top:-6px">“</span>
      <p>Lorem Ipsum is simply dummy text of the printing and typesetting industry. Lorem Ipsum has been the industry's standard dummy text ever...</p>
      <span class="qmark" style="right:0;top:56px">”</span>
      <span class="name">Marcus Hale</span><span class="role">Business man</span>
    </div>
  </div>
  <div class="dots"><span class="on"></span><span></span><span></span></div>
</section>

<footer class="site-footer">
  <div class="fcol" style="left:102px">
    <h5>Newsletter signup</h5>
    <p style="margin-top:6px">Get our recent updates through your email id</p>
    <div class="email-field">Enter your email id</div>
    <div class="btn-outline">Subscribe now</div>
  </div>
  <div class="fcol" style="left:479px">
    <h5>Welcome</h5>
    <ul><li>Home</li><li>About us</li><li>Services</li><li>What we do</li><li>Events</li><li>Gallery</li><li>Contact us</li></ul>
  </div>
  <div class="fcol" style="left:642px">
    <h5>Contact Info</h5>
    <ul>
      <li style="font-weight:600">Hire a Lantern</li>
      <li>120 STreet name, City name,</li>
      <li>Country name : 55501842</li>
      <li class="contact-line" style="margin-top:8px"><svg width="12" height="12" viewBox="0 0 12 12"><path d="M2.5 1l2 2.5-1.2 1.5a7 7 0 0 0 3.7 3.7L8.5 7.5 11 9.5 9.5 11C5 11 1 7 1 2.5z" fill="#fff"/></svg>(5550) 184 270</li>
      <li class="contact-line"><svg width="13" height="10" viewBox="0 0 13 10"><rect x=".7" y=".7" width="11.6" height="8.6" fill="none" stroke="#fff" stroke-width="1.3"/><path d="M1 1l5.5 4.5L12 1" fill="none" stroke="#fff" stroke-width="1.3"/></svg>hello@hirealantern.com</li>
    </ul>
  </div>
  <div class="fcol" style="left:916px">
    <h5>Follow Us</h5>
    <p style="margin-top:6px">Connect with our social network</p>
    <div class="socials"><span></span><span></span><span></span><span></span></div>
  </div>
</footer>

<div class="bottom-bar">
  <span>© 2016. Hire a Lantern. All rights reserved.</span>
  <span style="margin-left:14px">Terms &amp; Conditions</span><span>/</span><span>Privacy Policy</span><span>/</span><span>Disclaimer</span>
</div>

</body>
</html>
```